Presentation Folder Cover For Plumbing Company

We need a presentation folder cover (FRONT AND BACK) for our plumbing business.

We specialise in plumbing, hot water, electrical and pipe relining.

This will be sent to clients and the contents pages will outline all of our company details and information.

The target market for this cover is Strata / Property Managers who look after unit buildings.

Target Market(s)

Strata & Property Managers. The higher end of the property market.

Industry/Entity Type

Plumbing

Font styles to use
Sans Serif

Colors
ec1f27
0355a3
ffffff
474747
c9c9c9

Requirements
Must have
• A4 Paper Size
• Inviting to clients to open the document and read on.
Nice to have
• Sleek, Professional and Stands Out.
Should not have
• Dark Background. Needs to be fresh and bright.

```html
<!DOCTYPE html>
<html lang="en">
<head>
<meta charset="utf-8">
<title>Harbor Flow Services — Folder Cover</title>
<link href="https://fonts.googleapis.com/css2?family=Roboto:wght@400;700;900&display=swap" rel="stylesheet">
<style>
  :root {
    --brand-red: #ec1f27;
    --brand-blue: #0355a3;
    --white: #ffffff;
    --ink: #1a1a1a;
    --grey-dark: #474747;
    --grey-light: #c9c9c9;
    --sky-top: #eaf4fb;
    --sky-mid: #a9cfea;
    --sky-deep: #6fabd6;
  }
  html, body {
    margin: 0;
    padding: 0;
    width: 1200px;
    height: 849px;
    overflow: hidden;
    background: var(--white);
  }
  .cover {
    position: relative;
    width: 1200px;
    height: 849px;
    overflow: hidden;
    font-family: "Roboto", Arial, sans-serif;
  }
  .motion-photo {
    position: absolute;
    inset: 0;
    background:
      radial-gradient(ellipse 260px 220px at 900px 260px, rgba(255,255,255,1) 0%, rgba(255,255,255,0.9) 40%, rgba(255,255,255,0) 100%),
      linear-gradient(172deg,
        #c94a3a 0%, #e6873f 9%, #b8352f 15%, #d9a25a 22%, #c46a3c 30%,
        #8fb2cc 38%, #c8dcea 44%, rgba(210,230,244,1) 50%, var(--sky-mid) 70%, var(--sky-deep) 100%);
  }
  .motion-photo::after {
    content: "";
    position: absolute;
    inset: 0;
    background:
      linear-gradient(100deg, rgba(255,255,255,0) 55%, rgba(240,248,253,0.85) 68%, rgba(255,255,255,0.6) 80%, rgba(236,31,39,0.25) 100%);
  }
  .brand {
    position: absolute;
    left: 810px;
    top: 190px;
    width: 222px;
    text-align: center;
  }
  .brand-name {
    display: flex;
    align-items: center;
    justify-content: center;
    gap: 8px;
    font-weight: 900;
    font-size: 27px;
    line-height: 1.05;
    color: var(--brand-blue);
  }
  .brand-mark {
    width: 14px;
    height: 14px;
    background: var(--brand-red);
    border-radius: 50%;
    flex: none;
  }
  .brand-services {
    margin-top: 14px;
    font-weight: 700;
    font-size: 14.5px;
    color: var(--ink);
    white-space: nowrap;
  }
  .web-address {
    position: absolute;
    left: 223px;
    top: 803px;
    font-size: 10px;
    color: var(--ink);
  }
</style>
</head>
<body>
  <main class="cover">
    <div class="motion-photo" role="img" aria-label="Motion-blurred street scene with red and orange buildings streaking toward a bright white vanishing point over a pale blue road"></div>

    <div class="brand">
      <div class="brand-name"><span class="brand-mark"></span>Harbor Flow Services</div>
      <div class="brand-services">Plumbing • Electrical • Hot Water</div>
    </div>

    <div class="web-address">www.harborflowservices.com.au</div>
  </main>
</body>
</html>
```